Business Card Redesign

We would like to redesign our existing business cards.
The new design shall look:
ELEGANT, LUXURY, PROFESSIONAL
Reference:
YOU CAN VISIT WWW.LUMEN-RIVET.HK FOR BETTER UNDERSTANDING OF COMPANY STRATEGY AND POSITION
Additional:
CHOSEN CANDIDATE SHALL PROVIDE THE INSTRUCTION OF PRINTING IF ANY THERMAL COVERAGE OR ANY ADDITION IS OFFERED
Industry/Entity Type
Business

```html
<!DOCTYPE html>
<html lang="en">
<head>
<meta charset="utf-8">
<title>Lumen &amp; Rivet Limited – Business Card</title>
<link rel="stylesheet" href="https://fonts.googleapis.com/css2?family=Arimo:wght@400;700&display=swap">
<style>
  :root {
    --navy: #1e2a9a;
    --navy-deep: #17207f;
    --gold: #c99a0a;
    --gold-light: #d9ad2a;
    --white: #ffffff;
    --backdrop: #e6e6e4;
  }
  * { margin: 0; padding: 0; box-sizing: border-box; }
  html, body {
    width: 1200px; height: 1000px; overflow: hidden;
    background: var(--backdrop);
    font-family: "Arimo", Arial, sans-serif;
  }
  .card-set {
    position: absolute; top: 148px; left: 196px;
    display: flex; gap: 8px;
  }
  .card {
    position: relative; width: 400px; height: 704px;
  }
  .card--front { background: var(--navy); color: var(--white); }
  .card--back { background: var(--gold); }

  .brand-seal {
    position: absolute; left: 50%; transform: translateX(-50%);
    border-radius: 50%;
    display: flex; align-items: center; justify-content: center;
    text-align: center; font-weight: 700; text-transform: uppercase;
    line-height: 1.25; letter-spacing: 1px;
  }
  .card--front .brand-seal {
    top: 52px; width: 208px; height: 208px;
    background: var(--gold); color: var(--navy);
    font-size: 22px;
  }
  .card--back .brand-seal {
    top: 217px; width: 244px; height: 244px;
    background: var(--navy); color: var(--white);
    font-size: 25px;
  }

  .company-name {
    position: absolute; top: 270px; width: 100%;
    text-align: center; font-size: 22px; font-weight: 700;
  }
  .holder-name {
    position: absolute; top: 340px; width: 100%;
    text-align: center; font-size: 30px; font-weight: 700;
    color: var(--gold-light);
  }
  .holder-rule {
    position: absolute; top: 376px; left: 89px; width: 222px;
    height: 2px; background: var(--gold-light);
  }
  .holder-title {
    position: absolute; top: 382px; width: 100%;
    text-align: center; font-size: 16px; color: var(--gold-light);
  }
  .office-label {
    position: absolute; top: 444px; left: 62px;
    font-size: 21px;
  }
  .office-address {
    position: absolute; top: 478px; left: 62px; width: 270px;
    font-size: 16px; line-height: 26px;
    text-align: justify; text-align-last: justify;
  }
  .office-address span { display: block; }
  .contact-grid {
    position: absolute; top: 598px; left: 27px; right: 24px;
    display: flex; justify-content: space-between;
    font-size: 12px; line-height: 20px;
  }
  .website {
    position: absolute; top: 655px; width: 100%;
    text-align: center; font-size: 16px; color: var(--gold-light);
  }
</style>
</head>
<body>
  <main class="card-set">
    <section class="card card--front" aria-label="Card front">
      <div class="brand-seal">Lumen &amp;<br>Rivet<br>Limited</div>
      <p class="company-name">Lumen &amp; Rivet Limited</p>
      <p class="holder-name">Marisa Tong</p>
      <div class="holder-rule"></div>
      <p class="holder-title">PR Consultant</p>
      <p class="office-label">Headquarters (Hong Kong)</p>
      <p class="office-address">
        <span>Rm. 1204B, 12/F, Harbourlight Tower,</span>
        <span>18 Wellmoor Road, Central,</span>
        <span>Hong Kong</span>
      </p>
      <div class="contact-grid">
        <p>E-mail:marisa@lumen-rivet.hk<br>Mobile:(852) 9172 4408</p>
        <p>Tel:(852) 2740-3318<br>Fax: (852) 2740-3319</p>
      </div>
      <p class="website">www.lumen-rivet.hk</p>
    </section>
    <section class="card card--back" aria-label="Card back">
      <div class="brand-seal">Lumen &amp;<br>Rivet<br>Limited</div>
    </section>
  </main>
</body>
</html>
```